Cobalt Threads and Fuel is looking for a Clothing/Supplement Online Store Website!

Must be convenient, and user friendly, with vibrant colors that catch the eye!

Target Market(s)

Athletes, and Fashion Customers

Industry/Entity Type

Fitness

Coding

Coded - Design and coding required

Number of Pages Required

3 page

Font styles to use
Decorative

Colors

Designer to choose colors to be used in the design.

Requirements
Must have
• Somewhere to feature products, features to promote discounts and make announcements.
Nice to have
• My logos on each page

```html
<!DOCTYPE html>
<html lang="en">
<head>
<meta charset="utf-8">
<title>Cobalt Threads and Fuel</title>
<link href="https://fonts.googleapis.com/css2?family=Lato:wght@300;400;700;900&display=swap" rel="stylesheet">
<style>
:root{
  --ink:#222;
  --dark:#111;
  --bar:#333;
  --grey:#555;
  --mid:#777;
  --light:#eee;
  --line:#ccc;
  --white:#fff;
  --btn:#4a4a4a;
  --sale:#e53935;
  --bronze:#9a6240;
  --skin:#c0845a;
  --cyan:#5fb4e6;
  --orange:#e0562a;
}
*{box-sizing:border-box;margin:0;padding:0}
html,body{width:1200px;height:4114px;overflow:hidden}
body{font-family:"Lato",sans-serif;color:var(--ink);background:var(--white);position:relative}
.abs{position:absolute}

/* top bar */
.topbar{left:0;top:0;width:1200px;height:42px;background:var(--bar);color:#ddd;font-size:12px}
.topbar span{position:absolute;top:14px}
.topbar .sep{top:0;width:1px;height:42px;background:#555}

/* header */
.header{left:0;top:42px;width:1200px;height:98px;background:var(--white)}
.round-icon{width:48px;height:48px;border-radius:50%;background:var(--grey);display:flex;align-items:center;justify-content:center;flex-shrink:0}
.head-label{font-size:13px;color:var(--ink);line-height:20px}
.brand-plate{left:490px;top:0;width:220px;height:130px;background:var(--white);display:flex;align-items:center;justify-content:center;gap:8px;font-weight:900;font-size:36px;letter-spacing:1px;color:var(--bar)}
.brand-plate .dot{width:14px;height:14px;background:var(--bar)}

/* nav */
.nav{left:0;top:140px;width:1200px;height:45px;background:var(--light);display:flex;justify-content:center;gap:52px;align-items:center;font-size:17px;color:var(--mid)}
.nav .on{color:var(--grey)}

/* hero */
.hero{left:0;top:185px;width:1200px;height:615px}
.hero-logo{left:88px;top:312px;font-weight:900;font-size:56px;color:var(--white);letter-spacing:2px}
.hero-text{left:88px;top:380px;width:440px;font-size:22px;line-height:36px;color:var(--white)}
.btn-pill{left:89px;top:468px;width:204px;height:58px;border-radius:29px;background:var(--btn);color:var(--white);font-weight:700;font-size:17px;display:flex;align-items:center;justify-content:center;gap:8px}
.dots{left:88px;top:557px;display:flex;gap:9px}
.dots i{width:13px;height:13px;border-radius:50%;background:var(--white);display:block}
.dots i.cur{background:transparent;border:2px solid #999}

/* features */
.feature{width:250px;height:68px;border:1px solid var(--line);border-radius:34px;top:842px;display:flex;align-items:center;padding-left:6px;gap:12px}
.feature .round-icon{width:56px;height:56px}
.feature b{display:block;font-weight:400;font-size:13px;color:var(--ink)}
.feature small{font-size:12px;color:var(--mid)}

.section-title{left:0;width:1200px;text-align:center;font-size:36px;color:var(--grey);font-weight:400}

/* products */
.product{top:1050px;width:251px}
.product .shot{height:356px;position:relative}
.shot.hoodie-light{background:radial-gradient(ellipse 38% 36% at 50% 50%,#d9d9d9 0%,#e6e6e6 60%,#f3f3f3 100%)}
.shot.tub{background:radial-gradient(ellipse 28% 38% at 50% 52%,#0c0c0c 0%,#1c1c1c 70%,#3a3a3a 85%,#eeeeee 100%)}
.shot.hover{background:radial-gradient(ellipse 40% 38% at 50% 50%,#3a3a3a 0%,#555 55%,#8a8a8a 100%)}
.tag{position:absolute;top:14px;height:13px;font-size:8px;line-height:13px;color:var(--white);padding:0 5px}
.tag.sale{left:14px;background:var(--sale)}
.tag.new{right:14px;background:var(--dark)}
.product h3{font-weight:400;font-size:20px;text-align:center;margin-top:14px;color:var(--ink)}
.product p{font-size:15px;text-align:center;margin-top:4px}
.act{position:absolute;top:276px;height:26px;font-size:12px;color:var(--white);line-height:26px;padding:0 8px}

/* apparel banner */
.apparel{left:0;top:1529px;width:1200px;height:518px;background:
  radial-gradient(ellipse 18% 34% at 77% 48%,rgba(140,205,240,.85) 0%,rgba(95,180,230,.35) 55%,rgba(95,180,230,0) 100%),
  radial-gradient(ellipse 30% 50% at 88% 25%,rgba(120,170,210,.55) 0%,rgba(120,170,210,0) 100%),
  linear-gradient(90deg,#0b1826 0%,#1a3656 45%,#2d5a84 75%,#1e3c5c 100%)}
.apparel-title{left:88px;top:1686px;font-weight:700;font-size:46px;color:var(--white)}
.apparel-text{left:88px;top:1762px;width:470px;font-weight:700;font-size:17px;line-height:30px;color:var(--white)}
.btn-sq{background:var(--btn);color:var(--white);font-size:17px;display:flex;align-items:center;justify-content:center;border-radius:3px}

/* promo */
.promo{color:var(--white)}
.promo small{display:block;font-size:22px}
.promo strong{display:block;font-weight:400;font-size:30px;margin-top:2px}
.promo u{display:block;font-weight:700;font-size:15px;margin-top:6px}
.promo-women{background:
  radial-gradient(ellipse 30% 38% at 70% 60%,rgba(200,200,205,.55) 0%,rgba(200,200,205,0) 100%),
  radial-gradient(ellipse 14% 14% at 80% 22%,rgba(192,132,90,.7) 0%,rgba(192,132,90,0) 100%),
  linear-gradient(135deg,#4a4a4a,#1a1a1a)}
.promo-men{background:
  radial-gradient(ellipse 22% 50% at 76% 60%,rgba(192,132,90,.85) 0%,rgba(192,132,90,0) 100%),
  radial-gradient(ellipse 30% 70% at 76% 45%,rgba(200,200,200,.5) 0%,rgba(200,200,200,0) 100%),
  linear-gradient(90deg,#050505 45%,#222)}
.promo-supp{background:
  radial-gradient(ellipse 20% 40% at 68% 62%,rgba(220,190,110,.9) 0%,rgba(180,90,40,.8) 45%,rgba(180,90,40,0) 100%),
  linear-gradient(90deg,#1a1a1a 40%,#3a2a1c)}

/* supplement */
.supp{left:0;top:2713px;width:1200px;height:518px;background:
  radial-gradient(ellipse 10% 16% at 46% 38%,rgba(230,90,45,1) 0%,rgba(224,86,42,.6) 60%,rgba(224,86,42,0) 100%),
  radial-gradient(ellipse 22% 48% at 24% 58%,rgba(185,120,80,.95) 0%,rgba(150,90,60,.6) 55%,rgba(150,90,60,0) 100%),
  linear-gradient(90deg,#2a3644 0%,#151c25 50%,#0a0c10 100%)}
.supp-block{left:740px;top:2835px;width:340px;text-align:center;color:var(--white)}
.supp-block h2{font-weight:400;font-size:46px}
.supp-block hr{width:26px;border:0;border-top:2px solid var(--white);margin:16px auto 18px}
.supp-block p{font-size:17px;line-height:35px}

/* brands */
.brand-box{top:3351px;width:187px;height:109px;border:1px solid var(--line);display:flex;align-items:center;justify-content:center;font-size:24px;color:var(--bar);gap:8px}
.brand-box.shade{background:#f5f5f5}

/* footer */
.footer{left:0;top:3508px;width:1200px;height:606px}
.footer-text{color:var(--white);text-align:center}
.contact h4{font-weight:400;font-size:22px}
.contact p{font-size:13px;line-height:21px;margin-top:14px}
.social{top:3688px;width:32px;height:32px;background:var(--grey);border-radius:2px}
.card{top:3700px;width:30px;height:18px;border-radius:2px}
.bottom-links{top:4066px;font-size:13px;color:var(--white)}
</style>
</head>
<body>

<div class="abs topbar">
  <span style="left:100px">&#9679; Store Location</span>
  <span style="left:221px">&#9632; Track Your Order</span>
  <span style="left:368px">&#9679; Login / Register</span>
  <i class="abs sep" style="left:490px"></i>
  <i class="abs sep" style="left:810px"></i>
  <span style="left:818px">&#9990; Hotline: +1 555 010 2040</span>
  <span style="left:995px">English &#9662;</span>
  <span style="left:1068px">USD &#9662;</span>
</div>

<div class="abs header">
  <div class="abs round-icon" style="left:207px;top:25px">
    <svg width="22" height="22" viewBox="0 0 22 22"><circle cx="9" cy="9" r="6.5" fill="none" stroke="#fff" stroke-width="2.4"/><line x1="14" y1="14" x2="20" y2="20" stroke="#fff" stroke-width="2.6"/></svg>
  </div>
  <div class="abs head-label" style="left:264px;top:28px">SEARCH<br><span style="color:var(--grey)">Enter search here</span></div>
  <div class="abs round-icon" style="left:827px;top:25px">
    <svg width="24" height="22" viewBox="0 0 24 22"><path d="M1 3h4l3 11h11l3-8H7" fill="none" stroke="#fff" stroke-width="2"/><circle cx="9" cy="18" r="2" fill="#fff"/><circle cx="18" cy="18" r="2" fill="#fff"/></svg>
  </div>
  <div class="abs head-label" style="left:885px;top:28px">MY CART<br><span>0 item - $0.00</span></div>
</div>
<div class="abs brand-plate"><span class="dot"></span>COBALT</div>

<nav class="abs nav">
  <span class="on">Protein</span><span>Performance</span><span>Weight Management</span><span>Vitamins &amp; Health</span><span>Clothing &amp; Accessories</span>
</nav>

<svg class="abs hero" viewBox="0 0 1200 615" role="img" aria-label="Photo of a man and a woman lifting dumbbells against a dark backdrop">
  <defs>
    <radialGradient id="heroBase" cx="0.7" cy="0.45" r="0.6"><stop offset="0" stop-color="#3a2b22"/><stop offset="1" stop-color="#0b0b0b"/></radialGradient>
    <radialGradient id="heroWarmA" cx="0.6" cy="0.45" r="0.16"><stop offset="0" stop-color="#b77a52" stop-opacity=".95"/><stop offset="1" stop-color="#7a4a30" stop-opacity="0"/></radialGradient>
    <radialGradient id="heroWarmB" cx="0.8" cy="0.5" r="0.17"><stop offset="0" stop-color="#c8926a" stop-opacity=".9"/><stop offset="1" stop-color="#8a5a3c" stop-opacity="0"/></radialGradient>
  </defs>
  <polygon points="0,0 1200,0 1200,497 600,615 0,497" fill="#4d4d4d"/>
  <polygon points="0,0 1200,0 1200,497 600,603 0,497" fill="url(#heroBase)"/>
  <polygon points="0,0 1200,0 1200,497 600,603 0,497" fill="url(#heroWarmA)"/>
  <polygon points="0,0 1200,0 1200,497 600,603 0,497" fill="url(#heroWarmB)"/>
</svg>
<div class="abs hero-logo">COBALT</div>
<div class="abs hero-text">Sed ut perspiciatis unde omnis iste natus error sit voluptatem accusanti</div>
<div class="abs btn-pill">GET STARTED <span style="display:inline-block;width:16px;height:16px;border-radius:50%;background:#fff;color:var(--btn);font-size:11px;line-height:16px;text-align:center">&#10140;</span></div>
<div class="abs dots"><i></i><i></i><i class="cur"></i><i></i><i></i></div>

<div class="abs feature" style="left:75px">
  <div class="round-icon"><svg width="26" height="26" viewBox="0 0 26 26"><path d="M22 4c-6 0-11 4-13 10l3 3c6-2 10-7 10-13zM8 15l-4 1 3-5 3 0M11 18l-1 4 5-3 0-3" fill="#fff"/></svg></div>
  <div><b>FREE SHIPPING</b><small>On Orders Over $49.00</small></div>
</div>
<div class="abs feature" style="left:342px">
  <div class="round-icon"><svg width="28" height="20" viewBox="0 0 28 20"><rect x="1" y="2" width="26" height="16" rx="2" fill="none" stroke="#fff" stroke-width="2"/><circle cx="14" cy="10" r="4" fill="#fff"/></svg></div>
  <div><b>MONEY GUARANTEE</b><small>30 days back</small></div>
</div>
<div class="abs feature" style="left:608px">
  <div class="round-icon"><svg width="28" height="20" viewBox="0 0 28 20"><rect x="1" y="2" width="26" height="16" rx="2" fill="none" stroke="#fff" stroke-width="2"/><rect x="1" y="6" width="26" height="3" fill="#fff"/><rect x="5" y="12" width="8" height="2" fill="#fff"/></svg></div>
  <div><b>PAYMENT METHOD</b><small>Secure System</small></div>
</div>
<div class="abs feature" style="left:874px">
  <div class="round-icon"><svg width="26" height="24" viewBox="0 0 26 24"><path d="M4 16v-4a9 9 0 0 1 18 0v4" fill="none" stroke="#fff" stroke-width="2.4"/><rect x="2" y="14" width="6" height="8" rx="2" fill="#fff"/><rect x="18" y="14" width="6" height="8" rx="2" fill="#fff"/></svg></div>
  <div><b>ONLINE SUPPORT</b><small>24 hours a day</small></div>
</div>

<h2 class="abs section-title" style="top:966px">FEATURE PRODUCTS</h2>

<div class="abs product" style="left:75px">
  <div class="shot hoodie-light" role="img" aria-label="Grey hooded sweatshirt"><span class="tag sale">-20%</span><span class="tag new">New</span></div>
  <h3>Grouped Product</h3><p>$ 106.59</p>
</div>
<div class="abs product" style="left:342px">
  <div class="shot tub" role="img" aria-label="Black supplement tub"><span class="tag new">New</span></div>
  <h3>Grouped Product</h3><p>$ 106.59</p>
</div>
<div class="abs product" style="left:608px">
  <div class="shot hover" role="img" aria-label="Dark grey hooded sweatshirt">
    <span class="tag sale">-20%</span>
    <svg style="position:absolute;left:108px;top:160px" width="34" height="34" viewBox="0 0 34 34"><circle cx="17" cy="17" r="15" fill="none" stroke="#fff" stroke-width="1.5"/><path d="M17 10v14M10 17h14" stroke="#fff" stroke-width="1.5"/></svg>
    <span class="act" style="left:34px;background:var(--sale)">&#9829; WishList</span>
    <span class="act" style="left:128px;background:#555">&#9632; Add to Cart</span>
  </div>
  <h3>Grouped Product</h3><p>$ 106.59</p>
</div>
<div class="abs product" style="left:874px">
  <div class="shot tub" role="img" aria-label="Black supplement tub"><span class="tag sale">-20%</span><span class="tag new">New</span></div>
  <h3>Grouped Product</h3><p>$ 106.59</p>
</div>

<div class="abs apparel" role="img" aria-label="Photo of a woman training with battle ropes in a gym"></div>
<h2 class="abs apparel-title">Apparel</h2>
<p class="abs apparel-text">Lorem ipsum dolor sit amet, consecte adipiscing elit, sed do eiusmod tempor incididunt ut labore et dolore magna aliqua.</p>
<div class="abs btn-sq" style="left:88px;top:1864px;width:178px;height:47px">SHOP NOW</div>

<div class="abs promo-women" style="left:89px;top:2135px;width:470px;height:490px" role="img" aria-label="Photo of a woman in sportswear doing a lunge in a gym"></div>
<div class="abs promo" style="left:105px;top:2218px"><small>SHOP &amp; SAVE</small><strong>APPEAL WOMEN</strong><u>Explore Now</u></div>
<div class="abs promo-men" style="left:577px;top:2135px;width:534px;height:235px" role="img" aria-label="Photo of a man in an open hooded jacket"></div>
<div class="abs promo" style="left:599px;top:2200px"><small>SHOP &amp; SAVE</small><strong>APPEAL MEN</strong><u>Explore Now</u></div>
<div class="abs promo-supp" style="left:577px;top:2389px;width:534px;height:236px" role="img" aria-label="Photo of supplement powder in a bowl beside weight plates"></div>
<div class="abs promo" style="left:599px;top:2454px"><small>SHOP &amp; SAVE</small><strong>SUPPLEMENTS</strong><u>Explore Now</u></div>

<div class="abs supp" role="img" aria-label="Photo of a muscular man holding an orange shaker bottle"></div>
<div class="abs supp-block">
  <h2>Supplement</h2><hr>
  <p>Lorem ipsum dolor sit amet, consectetur adipiscing elit, sed do labore et dolore magna aliqua.</p>
  <div class="btn-sq" style="width:178px;height:50px;margin:20px auto 0">NEW ARRIVALS</div>
</div>

<h2 class="abs section-title" style="top:3275px">OUR BRAND</h2>
<svg class="abs" style="left:38px;top:3392px" width="40" height="26" viewBox="0 0 40 26"><path d="M39 13H3M14 2L3 13l11 11" fill="none" stroke="#444" stroke-width="2"/></svg>
<svg class="abs" style="left:1124px;top:3392px" width="40" height="26" viewBox="0 0 40 26"><path d="M1 13h36M26 2l11 11-11 11" fill="none" stroke="#444" stroke-width="2"/></svg>
<div class="abs brand-box" style="left:104px">Maple Row</div>
<div class="abs brand-box" style="left:305px"><span style="width:14px;height:14px;background:var(--bar)"></span>Ironworks</div>
<div class="abs brand-box" style="left:507px">Tallbox</div>
<div class="abs brand-box shade" style="left:708px">Pivot</div>
<div class="abs brand-box" style="left:909px">Norvane</div>

<svg class="abs footer" viewBox="0 0 1200 606" role="img" aria-label="Dark backdrop of a muscular figure behind the contact details">
  <defs><radialGradient id="footGlow" cx="0.5" cy="0.6" r="0.5"><stop offset="0" stop-color="#262626"/><stop offset="1" stop-color="#0a0a0a"/></radialGradient></defs>
  <polygon points="0,112 600,0 1200,112 1200,606 0,606" fill="#4d4d4d"/>
  <polygon points="0,118 600,12 1200,118 1200,606 0,606" fill="url(#footGlow)"/>
  <line x1="413" y1="420" x2="413" y2="500" stroke="#333"/>
  <line x1="767" y1="420" x2="767" y2="500" stroke="#333"/>
  <line x1="88" y1="530" x2="1128" y2="530" stroke="#444"/>
</svg>
<div class="abs card" style="left:89px;background:#3b6fd8"></div>
<div class="abs card" style="left:129px;background:#e0a030"></div>
<div class="abs card" style="left:171px;background:#5a8fd8"></div>
<div class="abs card" style="left:212px;background:#3455b8"></div>
<div class="abs social" style="left:895px"></div>
<div class="abs social" style="left:941px"></div>
<div class="abs social" style="left:985px"></div>
<div class="abs social" style="left:1031px"></div>
<div class="abs social" style="left:1076px"></div>

<div class="abs footer-text" style="left:0;top:3680px;width:1200px;font-weight:900;font-size:52px;letter-spacing:2px">COBALT</div>
<div class="abs footer-text" style="left:0;top:3780px;width:1200px;font-size:34px">CONTACT INFORMATIONS</div>

<div class="abs footer-text contact" style="left:88px;top:3860px;width:320px">
  <svg width="22" height="22" viewBox="0 0 22 22"><path d="M5 2l4 4-2 3c1 3 3 5 6 6l3-2 4 4-3 3C9 20 2 13 2 5z" fill="#fff"/></svg>
  <h4 style="margin-top:14px">CALL US</h4>
  <p>(+155)5 010 4471<br>(+155)5 010 4471</p>
</div>
<div class="abs footer-text contact" style="left:420px;top:3860px;width:360px">
  <svg width="22" height="22" viewBox="0 0 22 22"><path d="M11 2L1 11h3v9h5v-6h4v6h5v-9h3z" fill="#fff"/></svg>
  <h4 style="margin-top:14px">FIND US</h4>
  <p>No 12 Harbor Lane 45/1 Lakeview City,<br>NY, United States</p>
</div>
<div class="abs footer-text contact" style="left:795px;top:3860px;width:320px">
  <svg width="24" height="22" viewBox="0 0 24 22"><rect x="1" y="4" width="22" height="15" rx="2" fill="#fff"/><path d="M2 5l10 8 10-8" fill="none" stroke="#0a0a0a" stroke-width="1.6"/></svg>
  <h4 style="margin-top:14px">EMAIL</h4>
  <p>hello@cobaltfuel.example<br>care@cobaltfuel.example</p>
</div>

<div class="abs bottom-links" style="left:89px">Cobalt Threads and Fuel &copy; 2019. All Rights Reserved.</div>
<div class="abs bottom-links" style="left:622px;display:flex;gap:27px"><span>About</span><span>Legal infomation</span><span>Contact</span><span>Term of service</span><span>Privacy policy</span><span>C29</span></div>

</body>
</html>
```